Lakemont Vision Supply Post Card

Lakemont Vision Supply. We buy, sell and service ophthalmic equipment for the eye care professional.
We sell New and Pre-Owned Chairs and Stands, Slit Lamps, Refractors, , Autolensometers, Perimeters, Autrefractor/Keratometer, Retinal Cameras and many more.
We also do a equipment repair, preventive maintenance, practice relocation and set-up and in-office service calls.

Target Market(s)

Opthalmologists, optometrist and all eye care professionals.

Industry/Entity Type

Medical Equipment

Font styles to use
Sans Serif

Colors
0355a3
33a6d7

Requirements
Must have
• My web site address: www.lakemontvisionsupply.com, tel. 331-587-6490, email: lakemontsight@mailbrook.net.
• I will mail the postcard, i need space for the postage and recipient address on the back.
Nice to have
• https://www.sketchhub-example.com/design/20473815
• https://www.sketchhub-example.com/design/20473826
• https://www.sketchhub-example.com/design/20461937

```html
<!DOCTYPE html>
<html lang="en">
<head>
<meta charset="utf-8">
<title>Lakemont Vision Supply Postcard</title>
<link href="https://fonts.googleapis.com/css2?family=Oswald:wght@500;600;700&family=Lato:wght@400;700;900&display=swap" rel="stylesheet">
<style>
:root{
  --navy:#0355a3;
  --sky:#33a6d7;
  --sky-soft:#4b9fd3;
  --stage:#3d3d3d;
  --paper:#ffffff;
  --ink-grey:#555b60;
  --stamp:#e6e6e6;
}
*{margin:0;padding:0;box-sizing:border-box}
html,body{width:1200px;height:1200px;overflow:hidden;background:var(--stage)}
.canvas{position:relative;width:1200px;height:1200px}
.card{position:absolute;width:810px;height:524px;overflow:hidden;background:var(--paper);font-family:'Lato',sans-serif}
.card--front{left:115px;top:65px}
.card--back{left:281px;top:618px}
.abs{position:absolute}
.shapes{position:absolute;left:0;top:0}

/* brand name */
.brand{position:absolute;display:flex;align-items:center;gap:10px;font-family:'Lato',sans-serif;font-weight:400;color:var(--ink-grey);letter-spacing:2px;white-space:nowrap}
.brand__dot{flex:none;border-radius:50%;background:var(--ink-grey)}
.brand__name{text-align:center}
.card--front .brand{left:22px;top:26px;font-size:24px;line-height:34px}
.card--front .brand__dot{width:18px;height:18px}
.card--back .brand{left:462px;top:22px;font-size:17px;line-height:24px}
.card--back .brand__dot{width:13px;height:13px}

/* front */
.hero-title{left:13px;top:106px;font-family:'Oswald',sans-serif;font-weight:700;font-size:76px;line-height:1;color:var(--paper);letter-spacing:1px}
.hero-sub{left:13px;top:178px;font-family:'Oswald',sans-serif;font-weight:600;font-size:30px;line-height:34px;color:var(--paper)}
.services-tab{left:0;top:220px;width:170px;height:40px;background:var(--navy);clip-path:polygon(0 0,100% 0,88% 100%,0 100%)}
.services-tab span{position:absolute;left:13px;top:0;font-family:'Oswald',sans-serif;font-weight:500;font-size:27px;line-height:40px;color:var(--paper)}
.service-list{left:13px;top:266px;list-style:none;color:var(--paper);font-size:15.5px;line-height:19px}
.service-list li{display:flex;align-items:flex-start;gap:8px;margin-bottom:7px}
.service-list svg{flex:none;margin-top:2px}
.phone{display:flex;align-items:center;gap:8px;color:var(--paper);font-weight:700}
.card--front .phone{left:13px;top:410px;font-size:27px}
.contact{left:13px;color:var(--paper);display:flex;align-items:center;gap:8px}
.card--front .contact{font-size:15px}
.card--front .contact--mail{top:457px}
.card--front .contact--web{top:481px}

.photo{position:absolute}
.photo--backdrop{left:300px;top:0;width:510px;height:524px;background:linear-gradient(135deg,#f3f5f7 0%,#dfe4e9 45%,#c9d0d6 70%,#eef1f3 100%)}
.photo--chair{left:300px;top:200px;width:180px;height:300px;background:radial-gradient(ellipse at 50% 60%,#4a5056 0%,#8d969d 45%,rgba(170,180,188,0) 75%)}
.tile{position:absolute;width:134px;height:134px;background:var(--paper);border-radius:14px;transform:rotate(45deg);box-shadow:0 2px 6px rgba(0,0,0,.12)}
.tile .photo{left:30px;top:30px;width:74px;height:74px;border-radius:8px;transform:rotate(-45deg);background:radial-gradient(circle,#5f666c 0%,#a9b0b6 55%,#ffffff 80%)}
.tile--a{left:466px;top:12px}
.tile--b{left:514px;top:188px}
.tile--c{left:666px;top:144px}
.tile--d{left:626px;top:364px}

/* back */
.back-title{left:0;top:11px;width:232px;height:39px;background:var(--navy);clip-path:polygon(0 0,100% 0,91% 100%,0 100%)}
.back-title span{position:absolute;left:13px;top:0;font-family:'Oswald',sans-serif;font-weight:600;font-size:26px;line-height:39px;color:var(--paper)}
.back-lead{left:13px;top:60px;font-size:12px;font-weight:700;color:var(--paper)}
.back-body{left:13px;top:82px;width:402px;font-size:10.8px;line-height:14px;color:var(--paper);letter-spacing:-0.1px}
.back-body b{font-weight:700}
.back-strong{left:13px;top:178px;width:402px;font-size:12.2px;line-height:15.5px;font-weight:700;color:var(--paper)}
.support-title{left:100px;top:240px;width:220px;text-align:center;font-family:'Oswald',sans-serif;font-weight:600;font-size:22px;color:var(--navy)}
.support-item{position:absolute;text-align:center;color:var(--navy);font-family:'Oswald',sans-serif}
.support-item .photo{position:relative;margin:0 auto}
.support-item h3{font-weight:500;font-size:11px;line-height:13px}
.support-item p{font-family:'Lato',sans-serif;font-size:7px;line-height:9px}
.support-item--exam{left:2px;top:244px;width:116px}
.support-item--exam .photo{width:88px;height:110px;background:radial-gradient(ellipse at 50% 65%,#6e5a4a 0%,#a99c90 40%,rgba(255,255,255,0) 72%)}
.support-item--phoropter{left:114px;top:284px;width:184px}
.support-item--phoropter .photo{width:96px;height:78px;background:radial-gradient(ellipse,#3e4449 0%,#979fa5 50%,rgba(255,255,255,0) 74%)}
.support-item--tech{left:296px;top:246px;width:122px}
.support-item--tech .photo{width:64px;height:104px;background:radial-gradient(ellipse,#c8c4b6 0%,#e3e1d8 50%,rgba(255,255,255,0) 76%)}
.card--back .phone{left:15px;top:404px;font-size:32px}
.card--back .contact{font-size:17px}
.card--back .contact--mail{top:455px}
.card--back .contact--web{top:479px}
.stamp{left:717px;top:13px;width:80px;height:88px;background:var(--stamp)}
.address-line{position:absolute;left:588px;width:206px;height:1.5px;background:#222}
</style>
</head>
<body>
<main class="canvas">

  <!-- FRONT -->
  <section class="card card--front">
    <div class="photo photo--backdrop" role="img" aria-label="Soft-focus photo of ophthalmic examination equipment"></div>
    <svg class="shapes" width="810" height="524" viewBox="0 0 810 524" aria-hidden="true">
      <polygon points="0,0 310,0 397,100 0,100" fill="#ffffff"/>
      <polygon points="0,100 397,100 630,345 540,445 0,445" fill="var(--sky)"/>
      <polygon points="0,445 545,445 468,524 0,524" fill="var(--navy)"/>
    </svg>
    <div class="photo photo--chair" role="img" aria-label="Photo of an exam chair and instrument stand"></div>

    <div class="tile tile--a"><div class="photo" role="img" aria-label="Photo of a handheld autorefractor"></div></div>
    <div class="tile tile--b"><div class="photo" role="img" aria-label="Photo of an autolensometer"></div></div>
    <div class="tile tile--c"><div class="photo" role="img" aria-label="Photo of a phoropter"></div></div>
    <div class="tile tile--d"><div class="photo" role="img" aria-label="Photo of a slit lamp"></div></div>

    <div class="brand"><span class="brand__dot"></span><span class="brand__name">LAKEMONT VISION<br>SUPPLY</span></div>

    <h1 class="abs hero-title">WELCOME TO</h1>
    <h2 class="abs hero-sub">LAKEMONT VISION SUPPLY</h2>
    <div class="abs services-tab"><span>Our Services</span></div>

    <ul class="abs service-list">
      <li><svg width="15" height="15" viewBox="0 0 16 16"><circle cx="8" cy="8" r="8" fill="var(--navy)"/><path d="M4.5 8.2l2.3 2.3 4.7-4.8" stroke="#fff" stroke-width="1.8" fill="none"/></svg>Full Service Department</li>
      <li><svg width="15" height="15" viewBox="0 0 16 16"><circle cx="8" cy="8" r="8" fill="var(--navy)"/><path d="M4.5 8.2l2.3 2.3 4.7-4.8" stroke="#fff" stroke-width="1.8" fill="none"/></svg>Repair and Maintenance</li>
      <li><svg width="15" height="15" viewBox="0 0 16 16"><circle cx="8" cy="8" r="8" fill="var(--navy)"/><path d="M4.5 8.2l2.3 2.3 4.7-4.8" stroke="#fff" stroke-width="1.8" fill="none"/></svg>In-Office Service Calls</li>
      <li><svg width="15" height="15" viewBox="0 0 16 16"><circle cx="8" cy="8" r="8" fill="var(--navy)"/><path d="M4.5 8.2l2.3 2.3 4.7-4.8" stroke="#fff" stroke-width="1.8" fill="none"/></svg>Chairs and Stands, Lane Maintenance<br>and Urgent Repairs</li>
      <li><svg width="15" height="15" viewBox="0 0 16 16"><circle cx="8" cy="8" r="8" fill="var(--navy)"/><path d="M4.5 8.2l2.3 2.3 4.7-4.8" stroke="#fff" stroke-width="1.8" fill="none"/></svg>Practice Moves and Relocation's</li>
    </ul>

    <div class="abs phone">
      <svg width="22" height="22" viewBox="0 0 24 24"><circle cx="12" cy="12" r="10.5" fill="none" stroke="#fff" stroke-width="2"/><path d="M8.3 6.5l2 2.4-1.2 1.4c.8 1.8 2.2 3.2 4 4l1.4-1.2 2.4 2-1.3 1.9c-4.3-.5-8.1-4.3-8.6-8.6z" fill="#fff"/></svg>
      331-587-6490
    </div>
    <div class="abs contact contact--mail">
      <svg width="16" height="12" viewBox="0 0 16 12"><rect x="0.5" y="0.5" width="15" height="11" fill="#fff"/><path d="M1 1l7 5.5L15 1" stroke="var(--navy)" stroke-width="1.3" fill="none"/></svg>
      lakemontsight@mailbrook.net
    </div>
    <div class="abs contact contact--web">
      <svg width="15" height="15" viewBox="0 0 16 16" fill="none" stroke="#fff" stroke-width="1.3"><circle cx="8" cy="8" r="7"/><ellipse cx="8" cy="8" rx="3" ry="7"/><path d="M1 8h14M2.3 4.5h11.4M2.3 11.5h11.4"/></svg>
      www.lakemontvisionsupply.com
    </div>
  </section>

  <!-- BACK -->
  <section class="card card--back">
    <svg class="shapes" width="810" height="524" viewBox="0 0 810 524" aria-hidden="true">
      <defs>
        <linearGradient id="panelTone" x1="0" y1="0" x2="1" y2="1">
          <stop offset="0" stop-color="#3d8fcb"/>
          <stop offset="0.6" stop-color="#56a6d8"/>
          <stop offset="1" stop-color="#3f8ac4"/>
        </linearGradient>
      </defs>
      <path d="M0,0 H383 L518,140 Q537,166 522,196 L346,524 H0 Z" fill="var(--navy)"/>
      <path d="M0,0 H364 L496,138 Q513,164 500,190 L476,238 H0 Z" fill="#ffffff"/>
      <path d="M0,0 H360 L491,138 Q507,164 495,190 L472,238 H0 Z" fill="url(#panelTone)" role="img" aria-label="Faint photo of ophthalmic equipment behind text"/>
      <polygon points="0,238 476,238 395,397 0,397" fill="#ffffff"/>
      <polygon points="0,397 395,397 368,449 0,449" fill="var(--sky-soft)"/>
    </svg>

    <div class="abs back-title"><span>Lakemont Vision</span></div>
    <p class="abs back-lead">High-quality Ophthalmic Equipment &amp; Service!</p>
    <p class="abs back-body"><b>At Lakemont Vision,</b> we focus on taking care of everyone's precious gift to see the beauty of the world. Your job is fulfilling in a way that you can help your patients make proactive measures to take good care of their eyes or correct their issues, or even better, restore their vision. As much as you rely on your skills as an eye doctor, you also need the right state-of-the-art optical equipment that will help you guarantee top-notch medical services to your patients.</p>
    <p class="abs back-strong">Here at Lakemont Vision, you can get high-quality ophthalmic equipment as well as the accumulated knowledge of a veteran in the industry.</p>

    <h2 class="abs support-title">Service &amp; Support</h2>
    <div class="support-item support-item--exam">
      <div class="photo" role="img" aria-label="Photo of an exam room chair and stand"></div>
      <h3>Exam Room Equipment</h3>
      <p>Maintainence and Repair</p>
    </div>
    <div class="support-item support-item--phoropter">
      <div class="photo" role="img" aria-label="Photo of a phoropter"></div>
      <h3>Phoroptor Cleaning</h3>
      <p>Diassemby; Lens Cleaning; Lubrication; &amp; Calibration</p>
    </div>
    <div class="support-item support-item--tech">
      <div class="photo" role="img" aria-label="Photo of a desktop lensometer"></div>
      <h3>Technology Support</h3>
      <p>Cleaning &amp; Support</p>
    </div>

    <div class="abs phone">
      <svg width="26" height="26" viewBox="0 0 24 24"><circle cx="12" cy="12" r="10.5" fill="none" stroke="#fff" stroke-width="2"/><path d="M8.3 6.5l2 2.4-1.2 1.4c.8 1.8 2.2 3.2 4 4l1.4-1.2 2.4 2-1.3 1.9c-4.3-.5-8.1-4.3-8.6-8.6z" fill="#fff"/></svg>
      331-587-6490
    </div>
    <div class="abs contact contact--mail">
      <svg width="18" height="13" viewBox="0 0 16 12"><rect x="0.5" y="0.5" width="15" height="11" fill="#fff"/><path d="M1 1l7 5.5L15 1" stroke="var(--navy)" stroke-width="1.3" fill="none"/></svg>
      lakemontsight@mailbrook.net
    </div>
    <div class="abs contact contact--web">
      <svg width="17" height="17" viewBox="0 0 16 16" fill="none" stroke="#fff" stroke-width="1.3"><circle cx="8" cy="8" r="7"/><ellipse cx="8" cy="8" rx="3" ry="7"/><path d="M1 8h14M2.3 4.5h11.4M2.3 11.5h11.4"/></svg>
      www.lakemontvisionsupply.com
    </div>

    <div class="brand"><span class="brand__dot"></span><span class="brand__name">LAKEMONT VISION<br>SUPPLY</span></div>
    <div class="abs stamp" aria-label="Postage area"></div>
    <div class="address-line" style="top:216px"></div>
    <div class="address-line" style="top:250px"></div>
    <div class="address-line" style="top:284px"></div>
  </section>

</main>
</body>
</html>
```